New IT Consulting Company needs new Branding

I need some business cards and logo created for new IT consulting company called Copperline Partners Pty Ltd.

We deal with enterprise IT solution and IT consulting Firm.
Assisting businesses with Technology Upgrades and System integration

We have no existing color schemes in mind but after something a little recognizable but elegant also.

We are looking for something that conveys a professional look.

Target Market(s)

Targeting small to medium businesses with 0-500 employees

Industry/Entity Type

Information Technology

Contact Information for Business Card

Name, Title , Mobile Contact, Phone Contact , Email and Website URL

Logo Text

CopperPartners Pty Ltd "Shaping Smart Systems with care"

Font styles to use
Serif
Sans Serif

Requirements
Nice to have
• Looking for one or two primary colors and sticking to geometric or symmetrical design for the logo

```html
<!DOCTYPE html>
<html lang="en">
<head>
<meta charset="utf-8">
<title>Copperline Partners Pty Ltd – Business Cards</title>
<link rel="stylesheet" href="https://fonts.googleapis.com/css2?family=Tinos:wght@400;700&display=swap">
<style>
  :root {
    --backdrop: #e9e6e4;
    --card: #ffffff;
    --ink: #1b1b1b;
    --brand-blue: #2a4fa8;
    --link-blue: #2d4e8c;
    --accent-red: #e8302a;
    --accent-orange: #f57a1f;
    --accent-yellow: #f7b41f;
    --wave-blue: #1f5a8f;
  }
  * { box-sizing: border-box; margin: 0; padding: 0; }
  html, body { width: 1200px; height: 800px; overflow: hidden; }
  body {
    background: var(--backdrop);
    font-family: "Tinos", "Times New Roman", serif;
    color: var(--ink);
    display: flex;
    align-items: center;
    justify-content: center;
    gap: 40px;
  }
  .card {
    position: relative;
    width: 540px;
    height: 309px;
    background: var(--card);
    box-shadow: 0 10px 28px rgba(0,0,0,0.18);
    overflow: hidden;
  }
  /* Back of card */
  .card-back {
    display: flex;
    flex-direction: column;
    align-items: center;
    justify-content: center;
  }
  .brand {
    display: flex;
    align-items: center;
    gap: 12px;
    font-family: "Tinos", "Times New Roman", serif;
    font-weight: 700;
    color: var(--brand-blue);
    letter-spacing: 0.04em;
    text-transform: uppercase;
    line-height: 1.15;
  }
  .brand-mark {
    width: 34px;
    height: 34px;
    border: 3px solid var(--brand-blue);
    flex: none;
  }
  .card-back .brand { font-size: 25px; }
  .card-back .brand-name { max-width: 260px; }
  .website {
    margin-top: 34px;
    font-size: 15px;
    color: var(--link-blue);
  }
  /* Front of card */
  .holder {
    position: absolute;
    left: 34px;
    top: 30px;
  }
  .holder-name { font-size: 24px; font-weight: 400; }
  .holder-title { font-size: 14px; color: var(--accent-red); margin-top: 2px; }
  .contact {
    position: absolute;
    left: 34px;
    top: 116px;
    font-size: 13px;
    line-height: 1.35;
    list-style: none;
  }
  .contact .address { margin-bottom: 6px; }
  .contact li { display: flex; align-items: center; gap: 7px; }
  .contact svg { width: 11px; height: 11px; flex: none; }
  .card-front .brand {
    position: absolute;
    right: 30px;
    top: 108px;
    font-size: 19px;
  }
  .card-front .brand-name { max-width: 210px; }
  .card-front .brand-mark { width: 28px; height: 28px; }
  .wave {
    position: absolute;
    left: 0;
    bottom: 0;
    width: 540px;
    height: 309px;
  }
</style>
</head>
<body>

  <section class="card card-back">
    <div class="brand">
      <span class="brand-mark"></span>
      <span class="brand-name">Copperline Partners Pty Ltd</span>
    </div>
    <p class="website">www.copperlinepartners.com</p>
  </section>

  <section class="card card-front">
    <svg class="wave" viewBox="0 0 540 309" aria-hidden="true">
      <defs>
        <linearGradient id="flame" x1="0" y1="1" x2="1" y2="0">
          <stop offset="0" stop-color="var(--accent-red)"/>
          <stop offset="0.6" stop-color="var(--accent-orange)"/>
          <stop offset="1" stop-color="var(--accent-yellow)"/>
        </linearGradient>
      </defs>
      <path d="M150,309 C270,262 400,244 540,232 L540,309 Z" fill="url(#flame)"/>
      <path d="M200,272 C320,240 430,232 540,206 L540,214 C430,244 320,250 200,272 Z" fill="var(--wave-blue)"/>
    </svg>

    <div class="holder">
      <h1 class="holder-name">Your name here</h1>
      <p class="holder-title">Title here</p>
    </div>

    <ul class="contact">
      <li class="address">Address here,Address here<br>Address here</li>
      <li>
        <svg viewBox="0 0 12 12"><rect width="12" height="12" fill="var(--accent-red)"/><path d="M3.2 2.5l1.4 0 .6 1.8-.9.6a5 5 0 0 0 2.8 2.8l.6-.9 1.8.6v1.4c-3.5.3-6.6-2.8-6.3-6.3z" fill="#fff"/></svg>
        0312-4408-1956
      </li>
      <li>
        <svg viewBox="0 0 12 12"><rect width="12" height="12" fill="var(--accent-red)"/><rect x="4" y="2" width="4" height="8" rx="0.8" fill="none" stroke="#fff" stroke-width="1"/></svg>
        0467-2291-7730
      </li>
      <li>
        <svg viewBox="0 0 12 12"><rect width="12" height="12" fill="var(--accent-red)"/><rect x="2.5" y="3.5" width="7" height="5" fill="none" stroke="#fff" stroke-width="0.9"/><path d="M2.5 3.5l3.5 3 3.5-3" fill="none" stroke="#fff" stroke-width="0.9"/></svg>
        hello@copperlinepartners.com
      </li>
      <li>
        <svg viewBox="0 0 12 12"><rect width="12" height="12" fill="var(--accent-red)"/><circle cx="6" cy="6" r="3.4" fill="none" stroke="#fff" stroke-width="0.9"/><path d="M2.6 6h6.8M6 2.6c-1.6 2-1.6 4.8 0 6.8M6 2.6c1.6 2 1.6 4.8 0 6.8" fill="none" stroke="#fff" stroke-width="0.7"/></svg>
        copperlinepartners.com
      </li>
    </ul>

    <div class="brand">
      <span class="brand-mark"></span>
      <span class="brand-name">Copperline Partners Pty Ltd</span>
    </div>
  </section>

</body>
</html>
```